Varnecke Holdings Webpage Design

We need a new website for our company. The company is Varnecke Holdings Pty Ltd. We are in the business of Asbestos Removal; Demolition; Earthworks and Transport. We do not advertise and would like our website to be a reference point for our clients / potential clients and also to make our services known to those searching the internet for the services we offer. Some examples of the style of website we are after are:
http://www.quillmarkwrecking.example.au/
http://m.tovrinbrookclearing.example.au/
http://www.pellowayclearance.example.au
http://www.zorvat.example.au
http://www.kjbworks.example.au
http://www.northpeak-dismantling.example.au
We will need to work on content. Enclosed is an example. We also need to purchase the domain varneckeholdings.example.au and need to set up email accounts and ensure the website is mobile friendly. We have a company logo and have built our business on delivering professional, quality services on time. We would like the webpage to be simple, informative and professional - black and white / grey themed. We would also like to add a photo gallery etc later.

Colors
000000
fcfcfc
959595
dddddd

Requirements
Must have
• Information regarding the services we provide

```html
<!DOCTYPE html>
<html lang="en">
<head>
<meta charset="utf-8">
<title>Varnecke Holdings</title>
<link href="https://fonts.googleapis.com/css2?family=Lato:wght@300;400;700;900&display=swap" rel="stylesheet">
<style>
:root{
  --brand:#a95c56;
  --black:#000000;
  --white:#fcfcfc;
  --grey:#959595;
  --light:#dddddd;
  --panel:#f3f3f3;
  --gallery:#e6e6e6;
  --text:#333333;
}
*{margin:0;padding:0;box-sizing:border-box}
html,body{width:757px;height:1200px;overflow:hidden}
body{position:relative;background:var(--white);font-family:"Lato",sans-serif;color:var(--text)}
.abs{position:absolute}
.topbar{left:0;top:0;width:757px;height:22px;background:var(--brand)}
.social{position:absolute;display:flex;gap:5px}
.social span{width:15px;height:15px;border-radius:50%;background:var(--white);display:block}
.header{left:0;top:22px;width:757px;height:69px;background:#fff}
.logo{left:62px;top:14px;font-size:25px;font-weight:400;letter-spacing:5px;color:var(--brand);line-height:1}
.logo-sub{left:62px;top:45px;width:260px;height:1px;background:var(--brand)}
.contact{right:65px;font-size:10px;color:#222;display:flex;align-items:center;gap:5px}
.nav{left:0;top:91px;width:757px;height:30px;background:var(--black);display:flex;padding-left:62px}
.nav a{color:#fff;text-decoration:none;font-weight:700;font-size:11px;letter-spacing:.6px;display:flex;align-items:center;justify-content:center;border-right:1px solid #333}
.nav a.active{background:var(--brand)}
.hero{left:0;top:121px;width:757px;height:291px;background:linear-gradient(180deg,#6f8f4a 0%,#a6b39a 40%,#c9c4b8 70%,#8a8578 100%)}
.hero-cap{left:0;top:370px;width:757px;height:42px;background:rgba(0,0,0,.55);color:#fff;font-size:19px;font-weight:700;text-align:center;line-height:42px}
.card{width:149px;height:144px;top:440px;background:#fff;box-shadow:0 0 3px rgba(0,0,0,.25)}
.card h3{height:25px;line-height:25px;text-align:center;color:#fff;background:var(--black);font-size:11.5px;font-weight:700;letter-spacing:.5px}
.card.active h3{background:var(--brand)}
.card .pic{height:69px;background:linear-gradient(160deg,#8a9bb0,#8b7560)}
.card p{font-size:7.8px;color:#555;text-align:center;margin-top:8px;line-height:1.3}
.card .more{display:block;text-align:center;color:var(--brand);font-size:7.5px;margin-top:6px}
.welcome{left:0;top:606px;width:757px;height:269px;background:var(--panel)}
.wel-h{left:64px;top:632px;font-size:16.5px;font-weight:900;color:#111;letter-spacing:.3px}
.wel-h em{font-style:normal;color:var(--brand);margin-left:4px}
.wel-rule{left:64px;top:656px;width:379px;height:1px;background:#ccc}
.wel-rule::before{content:"";position:absolute;left:0;top:-1px;width:28px;height:2px;background:var(--brand)}
.wel-p{left:64px;top:668px;width:380px;font-size:8.6px;line-height:15.5px;color:#333}
.ticks{left:64px;top:735px;list-style:none;font-size:8.4px;color:#333}
.ticks li{height:21px;display:flex;align-items:center;gap:6px}
.btn{background:var(--brand);color:#fff;font-weight:700;border-radius:2px;display:flex;align-items:center;justify-content:center}
.inq{left:482px;top:634px;width:212px;height:209px;background:#fff;box-shadow:0 0 2px rgba(0,0,0,.15)}
.inq h2{height:28px;background:var(--brand);color:#fff;font-size:15.5px;font-weight:900;letter-spacing:.8px;padding-left:10px;line-height:28px}
.field{position:absolute;left:8px;width:196px;height:23px;border:1px dashed #ccc;display:flex;align-items:center;font-size:7.5px;color:#333}
.field i{width:22px;height:100%;background:#e8e8e8;margin-right:6px;display:flex;align-items:center;justify-content:center}
.gal{left:0;top:875px;width:757px;height:157px;background:var(--gallery)}
.gal-tab{left:292px;top:875px;width:171px;height:25px}
.gal-img{top:915px;width:149px;height:91px;background:linear-gradient(170deg,#5d88c0,#a99a7a)}
.arrow{color:#888;font-size:18px}
.footer{left:0;top:1032px;width:757px;height:141px;background:var(--black);color:#fff}
.fh{font-size:11.5px;font-weight:300;color:#ddd}
.fline{height:1px;background:#333}
.flist{list-style:none;font-size:7.8px;color:#ddd}
.flist li{height:16px;display:flex;align-items:center;gap:7px}
.flist li::before{content:"›";color:#777}
.ftext{font-size:7.8px;color:#eee;line-height:11px}
.copy{left:0;top:1173px;width:757px;height:27px;background:var(--brand);color:#fff;font-size:7.5px;text-align:center;line-height:27px}
</style>
</head>
<body>
<div class="abs topbar">
  <div class="social" style="left:610px;top:3px"><span></span><span></span><span></span><span></span></div>
</div>

<header class="abs header">
  <div class="abs logo">VARNECKE HOLDINGS</div>
  <div class="abs contact" style="top:22px">
    <svg width="10" height="10" viewBox="0 0 24 24"><path fill="#a95c56" d="M6.6 10.8a15 15 0 006.6 6.6l2.2-2.2c.3-.3.7-.4 1-.2 1.1.4 2.3.6 3.6.6.6 0 1 .4 1 1V20c0 .6-.4 1-1 1A17 17 0 013 4c0-.6.4-1 1-1h3.5c.6 0 1 .4 1 1 0 1.3.2 2.5.6 3.6.1.3 0 .7-.2 1z"/></svg>
    <span style="font-size:10.5px">0123-456-789</span>
  </div>
  <div class="abs contact" style="top:42px;font-size:8.5px">
    <svg width="13" height="9" viewBox="0 0 13 9"><rect width="13" height="9" fill="#a95c56"/><path d="M0 0l6.5 5L13 0" stroke="#fff" fill="none"/></svg>
    <span>names@varneckemail.example</span>
  </div>
</header>

<nav class="abs nav">
  <a class="active" style="width:76px">HOME</a>
  <a style="width:103px">ABOUT US</a>
  <a style="width:107px">SERVICES</a>
  <a style="width:104px">GALLERY</a>
  <a style="width:122px;border-right:none">CONTACT US</a>
</nav>

<div class="abs hero" role="img" aria-label="Worker hosing down a demolition site beside an excavator"></div>
<svg class="abs" style="left:22px;top:240px" width="24" height="53"><path d="M23 1L2 26l21 26" stroke="#fff" stroke-width="1.5" fill="none"/></svg>
<div class="abs hero-cap">Lorem Ipsum Dolor Sit Amet Consectetur Adipiscing Elit Duis Lac</div>

<div class="abs card active" style="left:65px"><h3>ASBESTOS REMOVAL</h3><div class="pic" role="img" aria-label="Workers in protective suits removing asbestos"></div><p>Ut wisi enim admn minim veniam,<br>quis nostrud exerci tation ulam</p><span class="more">Read More »</span></div>
<div class="abs card" style="left:224px"><h3>DEMOLITION</h3><div class="pic" role="img" aria-label="Excavator demolishing a building"></div><p>Ut wisi enim admn minim veniam,<br>quis nostrud exerci tation ulam</p><span class="more">Read More »</span></div>
<div class="abs card" style="left:384px"><h3>EARTHWORKS</h3><div class="pic" role="img" aria-label="Bulldozer and excavator moving earth"></div><p>Ut wisi enim admn minim veniam,<br>quis nostrud exerci tation ulam</p><span class="more">Read More »</span></div>
<div class="abs card" style="left:544px"><h3>TRANSPORT</h3><div class="pic" role="img" aria-label="Tipper truck on a work site"></div><p>Ut wisi enim admn minim veniam,<br>quis nostrud exerci tation ulam</p><span class="more">Read More »</span></div>

<section class="abs welcome"></section>
<h2 class="abs wel-h">WELCOME TO<em>VARNECKE HOLDINGS</em></h2>
<div class="abs wel-rule"></div>
<p class="abs wel-p">Lorem ipsum dolor sit amet, consectetur adipiscing elit. Duis lacinia, risus ac tincidunt eleifend, nequdfe ligula mattis sapien, ut scelerisque ligula ante vitae justo. Cras vehicula nisl lectus, at elementum arcufdsf luctus at. Nulla nec vehicula turpis, sit amet accumsan nisi. Maecenas nec accumsan mi. Proin sagittis leo tellus, malesuada placerat turpis rhoncus ut.</p>
<ul class="abs ticks">
  <li><svg width="9" height="8"><path d="M1 4l2.5 3L8 1" stroke="#a95c56" stroke-width="1.5" fill="none"/></svg>Lorem ipsum dolor sit amet, consectetuer adipiscing elit</li>
  <li><svg width="9" height="8"><path d="M1 4l2.5 3L8 1" stroke="#a95c56" stroke-width="1.5" fill="none"/></svg>Lorem ipsum dolor sit amet consectetuer</li>
  <li><svg width="9" height="8"><path d="M1 4l2.5 3L8 1" stroke="#a95c56" stroke-width="1.5" fill="none"/></svg>Lorem ipsum dolor sit amet consectetuer adipiscing</li>
  <li><svg width="9" height="8"><path d="M1 4l2.5 3L8 1" stroke="#a95c56" stroke-width="1.5" fill="none"/></svg>Lorem ipsum dolor sit amet consectetuer</li>
</ul>
<div class="abs btn" style="left:64px;top:820px;width:57px;height:19px;font-size:8.5px">Read More</div>

<form class="abs inq">
  <h2>QUICK INQUIRY</h2>
  <div class="field" style="top:38px"><i><svg width="10" height="10"><circle cx="5" cy="3" r="2.5" fill="#999"/><path d="M0 10a5 4 0 0110 0z" fill="#999"/></svg></i>Your Name</div>
  <div class="field" style="top:69px"><i><svg width="10" height="7"><rect width="10" height="7" fill="#999"/><path d="M0 0l5 4 5-4" stroke="#e8e8e8" fill="none"/></svg></i>Your Email</div>
  <div class="field" style="top:100px"><i><svg width="10" height="10" viewBox="0 0 24 24"><path fill="#999" d="M6.6 10.8a15 15 0 006.6 6.6l2.2-2.2c.3-.3.7-.4 1-.2 1.1.4 2.3.6 3.6.6.6 0 1 .4 1 1V20c0 .6-.4 1-1 1A17 17 0 013 4c0-.6.4-1 1-1h3.5c.6 0 1 .4 1 1 0 1.3.2 2.5.6 3.6.1.3 0 .7-.2 1z"/></svg></i>Phone</div>
  <div class="field" style="top:131px;height:36px;align-items:flex-start;padding-top:0"><i style="align-items:flex-start;padding-top:6px"><svg width="9" height="9"><path d="M1 8l1-3 5-5 2 2-5 5z" fill="#999"/></svg></i><span style="margin-top:8px">Message</span></div>
  <div class="btn" style="position:absolute;left:8px;top:184px;width:58px;height:19px;font-size:9.5px">SUBMIT</div>
</form>

<section class="abs gal"></section>
<svg class="abs gal-tab" viewBox="0 0 171 25"><path d="M0 0h171l-12 25H12z" fill="#a95c56"/><text x="85.5" y="17.5" text-anchor="middle" fill="#fff" font-family="Lato,sans-serif" font-weight="900" font-size="13.5" letter-spacing=".8">PROJECT GALLERY</text></svg>
<div class="abs arrow" style="left:45px;top:948px">‹</div>
<div class="abs gal-img" style="left:64px;background:#5f5a52" role="img" aria-label="Asbestos removal worker in a protective suit"></div>
<div class="abs" style="left:64px;top:938px;width:149px;text-align:center;color:#fff;font-weight:700;font-size:9.5px;line-height:14px">Lorem ipsum dolor sit<br>onsectetur adipiscing elit<br>Duis lacinia.</div>
<div class="abs gal-img" style="left:224px" role="img" aria-label="Excavator tearing down a building"></div>
<div class="abs gal-img" style="left:385px;background:linear-gradient(170deg,#6b5a3e,#a28e6a)" role="img" aria-label="Workers in protective suits inside a building"></div>
<div class="abs gal-img" style="left:545px" role="img" aria-label="Excavator loading a blue tipper truck"></div>
<div class="abs arrow" style="left:704px;top:948px">›</div>

<footer class="abs footer">
  <div class="abs fh" style="left:65px;top:13px">Quick Links</div>
  <div class="abs fline" style="left:65px;top:33px;width:76px"></div>
  <ul class="abs flist" style="left:65px;top:40px">
    <li>Home</li><li>About Us</li><li>Services</li><li>Gallery</li><li>Contact Us</li>
  </ul>
  <div class="abs fh" style="left:181px;top:13px">Contact Details</div>
  <div class="abs fline" style="left:181px;top:33px;width:139px"></div>

  <div class="abs ftext" style="left:185px;top:45px;display:flex;gap:6px"><svg width="7" height="10"><path d="M3.5 0a3.5 3.5 0 013.5 3.5C7 6 3.5 10 3.5 10S0 6 0 3.5A3.5 3.5 0 013.5 0z" fill="#a95c56"/></svg><span>Office 1<br>123 euismod cidun ut<br>gnak aliquam PG Feugait.</span></div>
  <div class="abs fline" style="left:181px;top:81px;width:140px"></div>
  <div class="abs ftext" style="left:187px;top:88px;display:flex;gap:7px;font-size:8.3px"><span style="color:#a95c56">✆</span>0123 - 456 - 789</div>
  <div class="abs fline" style="left:181px;top:104px;width:140px"></div>
  <div class="abs ftext" style="left:187px;top:112px;display:flex;gap:7px;align-items:center"><svg width="9" height="6"><rect width="9" height="6" fill="#a95c56"/></svg>names@varneckemail.example</div>

  <div class="abs ftext" style="left:367px;top:45px;display:flex;gap:6px"><svg width="7" height="10"><path d="M3.5 0a3.5 3.5 0 013.5 3.5C7 6 3.5 10 3.5 10S0 6 0 3.5A3.5 3.5 0 013.5 0z" fill="#a95c56"/></svg><span>Office 2<br>123 euismod cidun ut<br>gnak aliquam PG Feugait.</span></div>
  <div class="abs fline" style="left:363px;top:81px;width:142px"></div>
  <div class="abs ftext" style="left:366px;top:88px;display:flex;gap:7px;font-size:8.3px"><span style="color:#a95c56">✆</span>0123 - 456 - 789</div>
  <div class="abs fline" style="left:363px;top:104px;width:142px"></div>
  <div class="abs ftext" style="left:366px;top:112px;display:flex;gap:7px;align-items:center"><svg width="9" height="6"><rect width="9" height="6" fill="#a95c56"/></svg>names@varneckemail.example</div>

  <div class="abs" style="left:559px;top:68px;font-size:11px;letter-spacing:2.5px;color:#ccc;font-weight:400">VARNECKE HOLDINGS</div>
  <div class="social" style="left:592px;top:100px;gap:6px">
    <span style="width:19px;height:19px;background:var(--brand)"></span>
    <span style="width:19px;height:19px;background:var(--brand)"></span>
    <span style="width:19px;height:19px;background:var(--brand)"></span>
  </div>
</footer>
<div class="abs copy">Copyright © 2015 Varnecke Holdings | All Right Reserved.</div>
</body>
</html>
```